Need a fresh corporate identity for an existing Home Shopping Business in Thailand

We are one of the most active TV home shopping companies in Thailand. We need a fresh looking CI for our corporate, the colours of our corporate are Orange and Grey. We want our customers to see us as professional customer service who help them with their purchases.
The logo can be shown as a whole logo or either half logo but not less than half the logo.
Industry/Entity Type
Shopping
Requirements
Must have
- The logo should be shown at least half the logo or full logo.
Should not have
- The logo should not be shown less than half the logo.

```html
<!DOCTYPE html>
<html lang="en">
<head>
<meta charset="utf-8">
<title>BrightCart Stationery</title>
<link href="https://fonts.googleapis.com/css2?family=Open+Sans:wght@400;600;700&family=Exo+2:wght@400&display=swap" rel="stylesheet">
<style>
  :root{
    --orange:#e2642a;
    --grey:#a3a3a3;
    --ink:#4a4a4a;
    --paper:#ffffff;
    --backdrop:#ececec;
    --edge:#dcdcdc;
  }
  *{box-sizing:border-box;margin:0;padding:0}
  html,body{width:1200px;height:937px;overflow:hidden}
  body{background:var(--backdrop);font-family:"Open Sans",Arial,sans-serif;color:var(--ink);position:relative}
  .sheet{position:absolute;background:var(--paper);border:1px solid var(--edge);overflow:hidden}
  .footer-band{position:absolute;left:0;bottom:0;width:100%;background:linear-gradient(180deg,var(--grey) 0%,#c4a090 30%,var(--orange) 55%,var(--orange) 100%)}
  .brand-name{font-family:"Open Sans",Arial,sans-serif;font-weight:400;color:var(--orange);white-space:nowrap}
  .brand-dot{display:inline-block;border-radius:50%;background:var(--orange);vertical-align:middle}
  .url{position:absolute;font-family:"Exo 2",Arial,sans-serif;color:#fff;letter-spacing:3px;white-space:nowrap}

  /* letterhead */
  .letterhead{left:185px;top:68px;width:385px;height:544px}
  .letterhead .brand{position:absolute;left:36px;top:82px;font-size:14px}
  .letterhead .footer-band{height:90px}
  .contact-list{position:absolute;list-style:none;text-align:right;font-size:4.2px;line-height:7.6px;color:#555}
  .contact-list li::after{content:"";display:inline-block;width:5px;height:5px;border-radius:50%;background:var(--orange);margin-left:3px;vertical-align:middle}
  .letterhead .contact-list{right:12px;top:23px}
  .letter{position:absolute;left:36px;top:138px;width:300px;font-size:5px;line-height:7.6px;color:#555}
  .letter p{margin-bottom:9px}
  .letter .gap{margin-bottom:22px}
  .letter strong{font-weight:700}
  .signature{width:30px;height:18px;background:#f4f4f4;margin:4px 0 6px}

  /* folder */
  .folder{left:636px;top:41px;width:458px;height:576px}
  .folder .brand{position:absolute;left:0;right:0;top:356px;text-align:center;font-size:26px}
  .folder .brand-dot{width:14px;height:14px;margin-right:10px}
  .folder .footer-band{height:118px}
  .folder .url{right:16px;bottom:12px;font-size:11px}

  /* business cards */
  .card{border-radius:9px}
  .card-front{left:45px;top:658px;width:177px;height:100px}
  .card-front .brand{position:absolute;left:14px;top:18px;font-size:9px}
  .card-front .footer-band{height:42px}
  .card-front .person{position:absolute;left:18px;top:40px;font-size:5px;line-height:6px}
  .card-front .person .name{color:var(--orange);font-weight:600}
  .card-front .contact-list{left:100px;top:66px;text-align:left;font-size:3.6px;line-height:5.6px;color:#fff}
  .card-front .contact-list li::after{display:none}
  .card-front .contact-list li::before{content:"";display:inline-block;width:4px;height:4px;border-radius:50%;background:#fff;margin-right:3px;vertical-align:middle}
  .card-back{left:45px;top:785px;width:177px;height:100px;background:var(--orange);border-color:var(--orange)}
  .card-back .brand{position:absolute;left:0;right:0;top:40px;text-align:center;font-size:11px;color:#fff}

  /* envelope front */
  .envelope-front{left:265px;top:672px;width:432px;height:206px}
  .envelope-front .rule{position:absolute;left:22px;top:18px;height:92px;border-left:1px dotted #999}
  .envelope-front .brand{position:absolute;left:22px;top:90px;font-size:11px}
  .envelope-front .footer-band{height:80px}
  .envelope-front .url{right:22px;bottom:10px;font-size:9px}

  /* envelope back */
  .envelope-back{left:736px;top:672px;width:436px;height:206px}
  .flap{position:absolute;left:0;top:0;width:100%;height:71px;background:var(--orange);border-radius:0 0 34px 0}
  .envelope-back .url{left:0;right:0;top:27px;text-align:center;font-size:11px}
</style>
</head>
<body>

<section class="sheet letterhead">
  <div class="brand brand-name">BrightCart</div>
  <ul class="contact-list">
    <li>012 345 6789</li>
    <li>012 345 6780</li>
    <li>hello@brightcart.example</li>
    <li>www.brightcart.example</li>
    <li>12 Sample Lane, City Name 00000</li>
  </ul>
  <div class="letter">
    <p>July 2, 2012</p>
    <p><strong>Dear Ctr,</strong><br>ABC Building, del St., Country Name</p>
    <p>Thank you for choosing our team for your recent purchase. This letter confirms the details of your order and explains how our customer service staff can help you with delivery, returns and product questions. We aim to reply to every request within one working day, and our team is ready to guide you through each step of your purchase with care.</p>
    <p class="gap">Please keep this letter with your receipt. If any detail looks wrong, contact our service line and quote the order number shown above.</p>
    <p>We are always looking for ways to make shopping from home simpler. Our presenters test every product before it goes on air, and our call centre is open seven days a week. Should you need help later, simply call or write to us and a member of our team will be glad to assist you.</p>
    <p>Best Regards,</p>
    <div class="signature" role="img" aria-label="Handwritten signature"></div>
    <p><strong>Daniel Reyes</strong><br>Director<br><br>ABC Building, del St., Country Name</p>
  </div>
  <div class="footer-band" role="img" aria-label="Grey and orange decorative footer"></div>
</section>

<section class="sheet folder">
  <div class="brand brand-name"><span class="brand-dot"></span>BrightCart</div>
  <div class="footer-band" role="img" aria-label="Grey and orange decorative footer"></div>
  <div class="url">www.brightcart.example</div>
</section>

<section class="sheet card card-front">
  <div class="brand brand-name">BrightCart</div>
  <div class="person"><div class="name">NATE PORTER</div><div>Managing Director</div></div>
  <div class="footer-band" role="img" aria-label="Grey and orange decorative footer"></div>
  <ul class="contact-list">
    <li>012 345 6789</li>
    <li>012 345 6780</li>
    <li>hello@brightcart.example</li>
    <li>www.brightcart.example</li>
    <li>12 Sample Lane, City Name</li>
  </ul>
</section>

<section class="sheet card card-back">
  <div class="brand brand-name">BrightCart</div>
</section>

<section class="sheet envelope-front">
  <div class="rule"></div>
  <div class="brand brand-name">BrightCart</div>
  <div class="footer-band" role="img" aria-label="Grey and orange decorative footer"></div>
  <div class="url">www.brightcart.example</div>
</section>

<section class="sheet envelope-back">
  <div class="flap"></div>
  <div class="url">www.brightcart.example</div>
</section>

</body>
</html>
```